Trifold flyer for our dental clinic (the Bright Harbor Clinic)

The goal of this project is to design a trifold flyer for our dental clinic (the Bright Harbor Clinic). The winning design is expected to be creative, artistic and coherent with our logo.
Updates

Designs look the same

Target Market(s)

Young generation with dental need.

Industry/Entity Type

Dental Clinic

Font styles to use
Sans Serif

Colors
0355a3
85acd3
85cae6
0592cd
00a990
86cfc6
cedeed
cee9f5
cfeae6

Requirements
Must have
• See the attached sketch for content arrangement.

```html
<!DOCTYPE html>
<html lang="en">
<head>
<meta charset="utf-8">
<title>Bright Harbor Clinic – Trifold Flyer</title>
<link rel="stylesheet" href="https://fonts.googleapis.com/css2?family=Mulish:wght@600;700;800&family=Jost:wght@500;600&display=swap">
<style>
  :root {
    --brand-blue: #0355a3;
    --mid-blue: #0592cd;
    --sky-blue: #85acd3;
    --pale-blue: #cedeed;
    --white: #ffffff;
    --photo-warm: #c8784a;
    --photo-light: #e9e6e2;
  }
  * { margin: 0; padding: 0; box-sizing: border-box; }
  html, body { width: 1200px; height: 927px; overflow: hidden; background: var(--white); }
  .flyer {
    position: relative; width: 1200px; height: 927px; overflow: hidden;
    font-family: "Mulish", sans-serif; font-weight: 700; background: var(--white);
  }
  .block { position: absolute; }

  /* Left panel */
  .promos {
    left: 0; top: 0; width: 404px; height: 445px;
    background: linear-gradient(180deg, var(--brand-blue) 0%, #0a6ab8 100%);
    color: var(--white);
  }
  .promos h2, .services h2, .why h2, .info h2 {
    font-weight: 800; font-size: 24px; letter-spacing: 0.5px;
  }
  .promos h2 { position: absolute; left: 0; width: 404px; top: 36px; padding-left: 0; text-align: center; margin-left: -0px; }
  .promo { position: absolute; left: 74px; display: flex; gap: 11px; font-size: 15px; line-height: 18.2px; }
  .promo svg { flex: none; width: 25px; height: 25px; margin-top: -6px; }
  .photo-smile {
    left: 0; top: 453px; width: 404px; height: 131px;
    background: linear-gradient(90deg, #b24a1e 0%, #d98a52 25%, #f1d7c8 50%, #d98a52 75%, #a8641f 100%);
  }
  .services {
    left: 0; top: 591px; width: 404px; height: 336px;
    background: var(--pale-blue); color: var(--brand-blue); text-align: center;
  }
  .services h2 { position: absolute; top: 61px; width: 100%; }
  .services ul { position: absolute; top: 123px; width: 100%; list-style: none; font-size: 15.5px; line-height: 18.2px; font-weight: 700; }

  /* Middle panel */
  .photo-duo {
    left: 404px; top: 0; width: 394px; height: 163px;
    background: linear-gradient(90deg, #6b4331 0%, #e8d6c8 45%, #f4e3c2 60%, var(--photo-light) 100%);
  }
  .stripe { left: 404px; width: 394px; height: 8px; background: var(--brand-blue); }
  .why { left: 404px; top: 171px; width: 394px; height: 597px; color: var(--brand-blue); font-family: "Jost", sans-serif; }
  .why h2 { font-family: "Mulish", sans-serif; position: absolute; top: 62px; width: 100%; text-align: center; font-size: 24px; }
  .reason { position: absolute; left: 36px; width: 330px; display: flex; gap: 13px; font-size: 15.5px; line-height: 18.2px; font-weight: 500; letter-spacing: -0.2px; }
  .reason svg { flex: none; width: 19px; height: 19px; margin-top: -2px; }
  .photo-shades {
    left: 404px; top: 775px; width: 394px; height: 152px;
    background: linear-gradient(90deg, #c9461c 0%, #e48a4d 35%, #f0c2a0 55%, #c66631 100%);
  }

  /* Right panel */
  .info { left: 798px; top: 0; width: 402px; height: 522px; background: var(--sky-blue); color: var(--white); text-align: center; }
  .info h2 { position: absolute; width: 100%; line-height: 29px; }
  .info p { position: absolute; width: 100%; font-size: 15px; line-height: 18.2px; }
  .info .address { text-align: left; left: 122px; width: 260px; }
  .web { left: 798px; top: 530px; width: 402px; height: 397px; background: linear-gradient(180deg, #0573bd 0%, var(--mid-blue) 100%); color: var(--white); text-align: center; }
  .web h2 { position: absolute; top: 43px; width: 100%; font-size: 20px; font-weight: 800; }
  .web p { position: absolute; top: 75px; width: 100%; font-size: 15.5px; }
  .map {
    left: 837px; top: 658px; width: 328px; height: 224px; border-radius: 20px;
    background: linear-gradient(135deg, #f2f2f2 0%, #e6e6e6 55%, #cdeac0 100%);
    border: 6px solid var(--white);
  }
</style>
</head>
<body>
<div class="flyer">

  <section class="block promos">
    <h2>OUR PROMOS:</h2>
    <div class="promo" style="top:121px">
      <svg viewBox="0 0 24 24"><path d="M2 13 l6 7 L22 3 L8 15 Z" fill="#fff"/></svg>
      <div>$69 New Patient Secial<br>Includes: exam, cleaning,<br>and digital X Rays.<br>Regular Price $500</div>
    </div>
    <div class="promo" style="top:231px">
      <svg viewBox="0 0 24 24"><path d="M2 13 l6 7 L22 3 L8 15 Z" fill="#fff"/></svg>
      <div>$99 In-Office Teeth Whitening<br>Regular Price $700</div>
    </div>
    <div class="promo" style="top:303px">
      <svg viewBox="0 0 24 24"><path d="M2 13 l6 7 L22 3 L8 15 Z" fill="#fff"/></svg>
      <div>25% - 40% off ClearFit Aligners</div>
    </div>
    <div class="promo" style="top:358px">
      <svg viewBox="0 0 24 24"><path d="M2 13 l6 7 L22 3 L8 15 Z" fill="#fff"/></svg>
      <div>Plus Free Consultation!</div>
    </div>
  </section>

  <div class="block photo-smile" role="img" aria-label="Close-up photo of a smiling woman's mouth with a colorful scarf"></div>

  <section class="block services">
    <h2>OUR SERVICES:</h2>
    <ul>
      <li>- Cleaning And Prevention -</li>
      <li>- Cosmetic Dentistry -</li>
      <li>- Implant Dentistry -</li>
      <li>- Removable Dentures -</li>
      <li>- Orthodontics -</li>
      <li>- ClearFit Aligners -</li>
      <li>- Pediatric Dentistry -</li>
    </ul>
  </section>

  <div class="block photo-duo" role="img" aria-label="Photo of two young women laughing"></div>
  <div class="block stripe" style="top:163px"></div>

  <section class="block why">
    <h2>WHY CHOOSE US?</h2>
    <div class="reason" style="top:128px">
      <svg viewBox="0 0 20 20"><g stroke="#0355a3" stroke-width="3.2" stroke-linecap="round"><line x1="10" y1="1.5" x2="10" y2="18.5"/><line x1="2.6" y1="5.8" x2="17.4" y2="14.2"/><line x1="2.6" y1="14.2" x2="17.4" y2="5.8"/></g></svg>
      <div>Payment options and financial options are available!&nbsp; Most insurances are accepted!</div>
    </div>
    <div class="reason" style="top:219px">
      <svg viewBox="0 0 20 20"><g stroke="#0355a3" stroke-width="3.2" stroke-linecap="round"><line x1="10" y1="1.5" x2="10" y2="18.5"/><line x1="2.6" y1="5.8" x2="17.4" y2="14.2"/><line x1="2.6" y1="14.2" x2="17.4" y2="5.8"/></g></svg>
      <div>No Insurance?&nbsp; No Problem!&nbsp; Try our SMILE SAVINGS PLAN.&nbsp; With this plan, you can save from 80% to 100% on Preventative, Exam, X Rays, and Professional Cleaning.</div>
    </div>
    <div class="reason" style="top:365px">
      <svg viewBox="0 0 20 20"><g stroke="#0355a3" stroke-width="3.2" stroke-linecap="round"><line x1="10" y1="1.5" x2="10" y2="18.5"/><line x1="2.6" y1="5.8" x2="17.4" y2="14.2"/><line x1="2.6" y1="14.2" x2="17.4" y2="5.8"/></g></svg>
      <div>You can save 40% - 80 % on Fillings, Crowns, and In-Office Whitening.</div>
    </div>
    <div class="reason" style="top:455px">
      <svg viewBox="0 0 20 20"><g stroke="#0355a3" stroke-width="3.2" stroke-linecap="round"><line x1="10" y1="1.5" x2="10" y2="18.5"/><line x1="2.6" y1="5.8" x2="17.4" y2="14.2"/><line x1="2.6" y1="14.2" x2="17.4" y2="5.8"/></g></svg>
      <div>You can also save 25% - 65% on Advanced Dentures, Extractions, and Orthodontics (Braces).</div>
    </div>
  </section>

  <div class="block stripe" style="top:768px"></div>
  <div class="block photo-shades" role="img" aria-label="Photo of a smiling young woman wearing turquoise sunglasses"></div>

  <section class="block info">
    <h2 style="top:40px">CONVENIENT<br>SATURDAY HOURS!</h2>
    <p style="top:120px">Tuesday, Thursday<br>9:30 AM - 5:00 PM<br>Friday, Saturday<br>9:00 AM - 5:00 PM</p>
    <h2 style="top:260px">CALL US TODAY!</h2>
    <p style="top:304px">617.555.0142</p>
    <h2 style="top:379px">ADDRESS:</h2>
    <p class="address" style="top:422px">2750 Harbor Street<br>Suite 210<br>Lakeview, MA 02190</p>
  </section>

  <section class="block web">
    <h2>WEBSITE:</h2>
    <p>www.brightharborclinic.com</p>
  </section>

  <div class="block map" role="img" aria-label="Street map showing the clinic location"></div>

</div>
</body>
</html>
```